hi all

Im after a new age looking business card with my company logo on it

must include these details, I would like the PH and Email to be symbols

If the colours used for card could be kept within the colours used in logo that I have supplied that would be great, if another colour is to be used dark grey would be ok. no light bulbs etc thanks

Details below to be incorporated on card

Damian Holloway

Lic E871302

PH 0219647381

E info@brightvaleelectrical.example.nz

Domestic Commercial Industrial Electricians

```html
<!DOCTYPE html>
<html lang="en">
<head>
<meta charset="utf-8">
<title>Brightvale Electrical – Business Card Front</title>
<link rel="stylesheet" href="https://fonts.googleapis.com/css2?family=Open+Sans:wght@400;700&display=swap">
<style>
  :root {
    --brand-blue: #1176b9;
    --charcoal: #2a313b;
    --ink: #111111;
    --paper: #ffffff;
  }
  html, body {
    margin: 0;
    padding: 0;
    overflow: hidden;
    background: var(--paper);
  }
  .card {
    position: relative;
    width: 1200px;
    height: 686px;
    background: var(--paper);
    overflow: hidden;
    font-family: "Open Sans", sans-serif;
  }
  .brand {
    position: absolute;
    left: 0;
    right: 0;
    top: 270px;
    text-align: center;
    display: flex;
    justify-content: center;
    align-items: center;
    gap: 18px;
  }
  .brand-dot {
    width: 30px;
    height: 30px;
    border-radius: 50%;
    background: var(--brand-blue);
  }
  .brand-name {
    margin: 0;
    font-size: 44px;
    font-weight: 700;
    letter-spacing: 2px;
    text-transform: uppercase;
    color: var(--brand-blue);
    line-height: 1;
  }
  .tagline {
    position: absolute;
    left: 0;
    right: 0;
    top: 394px;
    margin: 0;
    text-align: center;
    font-size: 31px;
    font-weight: 400;
    color: var(--ink);
    transform: translateX(6px);
  }
  .base-bands {
    position: absolute;
    left: 0;
    bottom: 0;
    width: 1200px;
    height: 686px;
    display: block;
  }
  .band-dark { fill: var(--charcoal); }
  .band-blue { fill: var(--brand-blue); }
  .band-edge { stroke: var(--charcoal); stroke-width: 1.2; fill: none; }
</style>
</head>
<body>
  <main class="card">
    <div class="brand">
      <span class="brand-dot" aria-hidden="true"></span>
      <h1 class="brand-name">Brightvale Electrical</h1>
    </div>
    <p class="tagline">Domestic Commercial Industrial Electricians</p>

    <svg class="base-bands" viewBox="0 0 1200 686" aria-hidden="true">
      <polygon class="band-dark" points="0,516 600,574 1200,516 1200,686 0,686"/>
      <polygon class="band-blue" points="354,550 600,574 860,550 790,684 410,684"/>
      <polyline class="band-edge" points="354,550 600,574 860,550"/>
    </svg>
  </main>
</body>
</html>
```